Business Card Design

We are looking for a double sided business card.

On one side would be our logo

On the Other Side

Martin Kolby
Sales and Marketing

Phone/Text Logo and 530-418-2763
Email Logo and info@plumvalepets.com
Website Logo and www.plumvalepets.com
Facebook Logo and plumvale pets
Instagram Logo and plumvale_pets

Target Market(s)

Pet owners

Contact Information for Business Card

In project description

Requirements
Must have
• Logo

```html
<!DOCTYPE html>
<html lang="en">
<head>
<meta charset="utf-8">
<title>Plumvale Pets Business Card</title>
<link href="https://fonts.googleapis.com/css2?family=Montserrat:wght@400;500;700;800&display=swap" rel="stylesheet">
<style>
  :root {
    --canvas: #262628;
    --card: #1c1c1d;
    --card-edge: #2b2b2c;
    --silver: #dcdcdc;
    --white: #f2f2f2;
    --orange: #f39a1f;
    --orange-deep: #e8801a;
    --ghost: #2c2b2a;
  }
  * { box-sizing: border-box; margin: 0; padding: 0; }
  html, body { width: 1200px; height: 900px; overflow: hidden; }
  body {
    background: var(--canvas);
    font-family: "Montserrat", sans-serif;
    display: flex;
    flex-direction: column;
    align-items: center;
    justify-content: center;
    gap: 40px;
  }
  .card {
    position: relative;
    width: 700px;
    height: 400px;
    background: var(--card);
    border: 1px solid var(--card-edge);
    border-radius: 18px;
    overflow: hidden;
  }
  .ghost-name {
    position: absolute;
    font-weight: 800;
    color: var(--ghost);
    white-space: nowrap;
    letter-spacing: 2px;
  }
  /* front */
  .card--front .ghost-name { left: 40px; top: 150px; font-size: 92px; }
  .front-brand {
    position: absolute;
    left: 0; right: 0; top: 140px;
    text-align: center;
  }
  .brand-name {
    font-weight: 800;
    color: var(--silver);
    letter-spacing: 3px;
    white-space: nowrap;
  }
  .front-brand .brand-name { font-size: 62px; }
  .front-url {
    margin-top: 18px;
    font-size: 15px;
    font-weight: 700;
    letter-spacing: 6px;
    color: var(--orange);
  }
  /* back */
  .card--back .ghost-name { right: 30px; top: 60px; font-size: 58px; }
  .back-brand { position: absolute; left: 48px; top: 70px; }
  .back-brand .brand-name { font-size: 38px; }
  .person { position: absolute; left: 48px; top: 190px; }
  .person-name { font-size: 32px; font-weight: 700; color: var(--orange); }
  .person-title { font-size: 15px; font-weight: 500; color: var(--white); margin-top: 2px; }
  .rule {
    position: absolute;
    left: 48px; right: 30px; top: 272px;
    height: 2px;
    background: var(--orange-deep);
  }
  .contacts { position: absolute; left: 48px; top: 288px; list-style: none; }
  .contacts li {
    display: flex; align-items: center; gap: 12px;
    font-size: 16px; color: var(--white); line-height: 30px;
  }
  .contacts svg { width: 16px; height: 16px; flex: none; }
  .socials {
    position: absolute; right: 40px; top: 200px;
    padding-left: 22px;
    border-left: 1.5px solid var(--orange-deep);
    list-style: none;
  }
  .socials li {
    display: flex; align-items: center; gap: 10px;
    font-size: 16px; color: var(--white); line-height: 28px;
  }
  .dot { width: 13px; height: 13px; border-radius: 50%; background: var(--orange); flex: none; }
</style>
</head>
<body>
  <section class="card card--front" aria-label="Card front">
    <div class="ghost-name" aria-hidden="true">PLUMVALE</div>
    <div class="front-brand">
      <div class="brand-name">PLUMVALE PETS</div>
      <div class="front-url">WWW.PLUMVALEPETS.COM</div>
    </div>
  </section>

  <section class="card card--back" aria-label="Card back">
    <div class="ghost-name" aria-hidden="true">PLUMVALE</div>
    <div class="back-brand"><div class="brand-name">PLUMVALE PETS</div></div>
    <div class="person">
      <div class="person-name">Martin Kolby</div>
      <div class="person-title">Sales and Marketing</div>
    </div>
    <ul class="socials">
      <li><span class="dot"></span>@plumvale pets</li>
      <li><span class="dot"></span>@plumvale_pets</li>
    </ul>
    <div class="rule"></div>
    <ul class="contacts">
      <li>
        <svg viewBox="0 0 16 16"><path fill="#f39a1f" d="M3.5 1.5l2.5 0 1 3.5-1.6 1.2a9 9 0 0 0 4.4 4.4L11 9l3.5 1v2.5c0 1-.8 1.9-1.9 1.8C7 13.8 2.2 9 1.7 3.4 1.6 2.3 2.5 1.5 3.5 1.5z"/></svg>
        530-418-2763
      </li>
      <li>
        <svg viewBox="0 0 16 16"><rect x="1" y="3" width="14" height="10" rx="1.5" fill="#f39a1f"/><path d="M1.5 4l6.5 5 6.5-5" fill="none" stroke="#1c1c1d" stroke-width="1.4"/></svg>
        info@plumvalepets.com
      </li>
      <li>
        <svg viewBox="0 0 16 16"><circle cx="8" cy="8" r="6.5" fill="none" stroke="#f39a1f" stroke-width="1.5"/><ellipse cx="8" cy="8" rx="2.8" ry="6.5" fill="none" stroke="#f39a1f" stroke-width="1.2"/><path d="M1.5 8h13" stroke="#f39a1f" stroke-width="1.2"/></svg>
        www.plumvalepets.com
      </li>
    </ul>
  </section>
</body>
</html>
```